Heron Circle - Flyer boarder

I would like to have a sophisticated flyer that when everyone sees it they will know that it is connected to the Heron Circle because of the layout or design of the flyer. I would like something i can use over and over for different activities with at least one picture to add. I also think it is important to have our contact info, and heron circle logo imbedded into the layout or boarder.
Our activities have included Fire Pit Gathering, Lunch and Learn, Cedar Hat Weaving, Feather Beading, Headband Making, And we always like to include a picture of the activity we are putting out to the public for.

Thank You, Heron Circle.

Target Market(s)

Youth and their foster parents

Requirements
Must have
• Thick boarders breaking apart ideas on flyer.
Heron Circle Logo
Contact info: Tavik Heron Circle
Po Box 47 Port Alberni BC V9Y 3K8
Tel: (250) 555-0148 Toll-Free: 1-877-555-0163 Fax: (250) 555-0192
Nice to have
• backsplash..not necessary though.
Should not have
• dark/colored backgrounds. Limited printing budget.

```html
<!DOCTYPE html>
<html lang="en">
<head>
<meta charset="utf-8">
<title>Heron Circle – Fire Pit Gathering Flyer</title>
<link rel="stylesheet" href="https://fonts.googleapis.com/css2?family=Roboto+Condensed:wght@300;400;700&display=swap">
<style>
  :root {
    --red: #e42528;
    --black: #050505;
    --white: #ffffff;
    --page: #d9d9d9;
    --panel: rgba(8, 10, 14, 0.62);
    --night: #2f5f8f;
    --tree: #16241c;
    --gravel: #4a4a4c;
    --fire: #f59a2a;
  }
  * { margin: 0; padding: 0; box-sizing: border-box; }
  html, body { width: 1200px; height: 1200px; overflow: hidden; }
  body {
    background: var(--page);
    font-family: "Roboto Condensed", "Arial Narrow", sans-serif;
    position: relative;
  }
  .flyer {
    position: absolute;
    left: 150px; top: 17px;
    width: 900px; height: 1166px;
    background: var(--black);
    overflow: hidden;
  }
  .photo {
    position: absolute;
    left: 0; top: 250px;
    width: 900px; height: 740px;
    background:
      radial-gradient(ellipse 260px 150px at 430px 560px, rgba(245,154,42,.85), rgba(245,154,42,0) 70%),
      radial-gradient(ellipse 520px 260px at 620px 450px, rgba(190,120,80,.35), rgba(0,0,0,0) 70%),
      linear-gradient(180deg, var(--night) 0%, #3b6f9f 22%, var(--tree) 42%, #28342a 60%, var(--gravel) 80%, #2c2c2e 100%);
  }
  .band-top {
    position: absolute; left: 0; top: 0;
  }
  .title {
    position: absolute;
    left: 57px; top: 74px;
    color: var(--white);
    font-weight: 400;
    font-size: 81px;
    line-height: 70px;
    letter-spacing: 0.5px;
  }
  .logo-disc {
    position: absolute;
    left: 441px; top: -86px;
    width: 436px; height: 436px;
    border-radius: 50%;
    background: var(--white);
    display: flex; align-items: center; justify-content: center;
    padding-top: 86px;
  }
  .logo-name {
    color: var(--black);
    font-weight: 700;
    font-size: 46px;
    line-height: 50px;
    text-align: center;
  }
  .info-panel {
    position: absolute;
    left: 40px; top: 280px;
    width: 364px; height: 678px;
    background: var(--panel);
    color: var(--white);
  }
  .feature {
    position: absolute; left: 30px; top: 40px;
    font-weight: 700; font-size: 36px; white-space: nowrap;
  }
  .dot {
    display: inline-block;
    width: 20px; height: 20px;
    border-radius: 50%;
    background: var(--red);
    vertical-align: middle;
    margin-right: 15px;
    position: relative; top: -3px;
  }
  .feature-text {
    position: absolute; left: 30px; top: 91px;
    width: 320px;
    font-size: 18px; line-height: 25px; font-weight: 400;
  }
  .event-date {
    position: absolute; left: 0; top: 236px; width: 364px;
    text-align: center;
    font-size: 40px; font-weight: 400;
  }
  .activity-list {
    position: absolute; left: 22px; top: 320px;
    list-style: none;
    font-size: 27px; line-height: 47px;
  }
  .activity-list .dot { margin-right: 17px; }
  .call-label {
    position: absolute; left: 28px; top: 536px;
    font-size: 24px; white-space: nowrap;
  }
  .call-number {
    position: absolute; left: 24px; top: 572px;
    color: var(--red);
    font-weight: 700; font-size: 54px; letter-spacing: 0.5px;
  }
  .band-bottom { position: absolute; left: 0; top: 940px; }
  .footer {
    position: absolute; left: 0; top: 990px; width: 900px;
    text-align: center; color: var(--white);
  }
  .tags { font-size: 22px; line-height: 35px; }
  .tags .sep {
    display: inline-block; width: 9px; height: 9px; border-radius: 50%;
    background: var(--red); margin: 0 14px; vertical-align: middle;
  }
  .register { font-size: 23px; margin-top: 9px; letter-spacing: 0.3px; }
  .website { color: var(--red); font-size: 29px; margin-top: 5px; }
</style>
</head>
<body>
  <div class="flyer">
    <div class="photo" role="img" aria-label="Photo of a family gathered in chairs around an outdoor fire pit at dusk"></div>

    <svg class="band-top" width="900" height="300" viewBox="0 0 900 300" aria-hidden="true">
      <polygon fill="var(--red)" points="0,0 900,0 900,250 600,250 560,262 520,252 480,270 440,258 400,276 360,262 320,280 290,266 250,284 210,270 170,280 130,268 90,282 50,270 20,284 0,276"/>
    </svg>

    <h1 class="title">HERON<br>CIRCLE</h1>

    <div class="logo-disc">
      <div class="logo-name">Tavik<br>Heron Circle</div>
    </div>

    <section class="info-panel">
      <h2 class="feature"><span class="dot"></span>Fire Pit Gathering</h2>
      <p class="feature-text">A crowd-pleaser for both kids and adults, a s'mores party is the perfect idea for gathering everyone around the fire pit. Collect some long sticks from your yard to .</p>
      <p class="event-date">11/05/2021</p>
      <ul class="activity-list">
        <li><span class="dot"></span>Lunch and Learn</li>
        <li><span class="dot"></span>Cedar Hat Weaving</li>
        <li><span class="dot"></span>Feather Beading</li>
        <li><span class="dot"></span>Headband Making</li>
      </ul>
      <p class="call-label">FOR MORE INFO CALL US NOW</p>
      <p class="call-number">2505550148</p>
    </section>

    <svg class="band-bottom" width="900" height="226" viewBox="0 0 900 226" aria-hidden="true">
      <polygon fill="var(--black)" points="0,22 30,12 60,26 100,18 140,30 190,20 240,34 290,24 340,38 400,30 460,40 520,32 580,42 640,34 700,44 760,36 820,46 870,38 900,44 900,226 0,226"/>
      <polyline fill="none" stroke="var(--red)" stroke-width="4" points="0,22 30,12 60,26 100,18 140,30 190,20 240,34 290,24 340,38 400,30 460,40 520,32 580,42 640,34 700,44 760,36 820,46 870,38 900,44"/>
    </svg>

    <footer class="footer">
      <p class="tags">Culture<span class="sep"></span>Family<span class="sep"></span>Exercise<span class="sep"></span>Crafts<span class="sep"></span>Regalia<span class="sep"></span>Song<span class="sep"></span>Dance<span class="sep"></span>Language</p>
      <p class="tags">Protocol<span class="sep"></span>Cooking<span class="sep"></span>Laughs<span class="sep"></span>Jokes<span class="sep"></span>Humour<span class="sep"></span>FUN!</p>
      <p class="register">REGISTER TO ATTEND ANY OR ALL OF OUR ACTIVITES !</p>
      <p class="website">www.yourwebsitehere.com</p>
    </footer>
  </div>
</body>
</html>
```